Clearway Lung Institute of Houston Brochures

We need a redesign of our Brochures. We want to merge the two current brochure ideas into one cohesive, simple, and bold design. Notice that one design is generic and educational about Pulmonary Rehab in general. The other has our company branding and logo throughout. The front of the brochure needs to do better job of catching attention. We like the slogan: "Don't fight Shortness of Breathe Alone." The majority of our patients talk about how lonely the journey is dealing with chronic lung disease and shortness of breath. We have also updated our Logo since the last brochure design.
These brochures will be in Pulmonary Doctor waiting rooms and patient rooms.

Target Market(s)

Seniors 50+ with chronic lung disease in Houston Texas.

Industry/Entity Type

HealthCare

Colors
0054AA
0677BA
7BADD7
CADEEF
E8F1F8

Requirements
Must have
• Must have locations of 5 clinics. Must have visuals that aid in describing benefits of Pulmonary Rehab and Why pulmonary Rehab is right for them.
Nice to have
• Simple design. concise. Educational, yet not information overload.

```html
<!DOCTYPE html>
<html lang="en">
<head>
<meta charset="utf-8">
<title>Clearway Lung Institute of Houston – Brochure Inside Page</title>
<link href="https://fonts.googleapis.com/css2?family=Roboto:wght@300;400&display=swap" rel="stylesheet">
<style>
  :root{
    --board:#38383a;
    --navy:#1f4f9a;
    --blue:#0054aa;
    --sky:#0677ba;
    --mid:#7badd7;
    --pale:#cadeef;
    --mist:#e8f1f8;
    --ink:#1d1d1f;
    --text:#3a3a3c;
    --white:#ffffff;
  }
  *{margin:0;padding:0;box-sizing:border-box}
  html,body{width:1200px;height:849px;overflow:hidden;background:var(--board)}
  body{position:relative;font-family:'Roboto',Arial,sans-serif;color:var(--text)}
  .spread{position:absolute;left:200px;top:116px;width:798px;height:616px;overflow:hidden;
    background:linear-gradient(180deg,#cfe0f1 0%,#e6eff8 45%,#f3f7fb 70%,#dde9f5 100%)}
  .spread-bands{position:absolute;inset:0}
  .label{position:absolute;left:199px;top:742px;font-size:23px;font-weight:400;color:var(--white)}
  .brand{position:absolute;font-weight:400;letter-spacing:1px}
  .brand-program{left:60px;top:56px;width:250px;text-align:center;font-size:22px;color:var(--navy);line-height:1.2}
  .brand-clinic{left:461px;top:58px;display:flex;align-items:center;gap:10px;font-size:17px;color:var(--sky);line-height:1.15}
  .brand-clinic .dot{width:26px;height:26px;border-radius:50%;background:var(--sky);flex:none}
  h2{position:absolute;font-weight:300;color:var(--blue);line-height:1;white-space:nowrap}
  .intro-title{left:44px;top:128px;font-size:21px}
  .intro-body{position:absolute;left:44px;top:152px;width:350px;font-size:11.2px;font-weight:300;line-height:12px;color:var(--text);white-space:nowrap}
  .steps-title{left:44px;top:219px;font-size:20px}
  .way-title{left:207px;top:219px;font-size:20px}
  .steps-body{position:absolute;left:44px;top:241px;width:165px;font-size:11.2px;font-weight:300;line-height:12px;white-space:nowrap}
  .bullets{position:absolute;list-style:none;font-size:8.3px;color:var(--ink);z-index:2}
  .bullets li{position:relative;padding-left:9px}
  .bullets li::before{content:"";position:absolute;left:1px;top:2px;width:3px;height:3px;background:var(--ink)}
  .steps-list{left:44px;top:315px;line-height:10px}
  .steps-list li{margin-bottom:7px}
  .way-list{left:207px;top:245px;width:180px;line-height:10.5px}
  .way-list li{margin-bottom:9.5px}
  .photo{position:absolute;left:36px;top:368px;width:340px;height:248px;z-index:1;
    background:linear-gradient(160deg,#e9ddd2 0%,#c9d9e8 45%,#f0c6c8 100%);border-radius:60px 60px 0 0}
  .why-title{left:446px;top:120px;font-size:23px}
  .card{position:absolute;left:423px;width:320px;border:1px solid rgba(255,255,255,.9);border-radius:14px;
    background:rgba(255,255,255,.35);padding:10px 0 0 22px}
  .card h3{font-size:14.6px;font-weight:400;color:var(--ink);margin-bottom:2px;white-space:nowrap}
  .card li{list-style:none;font-size:11px;font-weight:300;line-height:15.7px;color:var(--text);white-space:nowrap}
  .card li::before{content:"▪";font-size:8px;margin-right:1px}
  .card p{font-size:11px;font-weight:300;line-height:13.1px;white-space:nowrap}
  .card-breath{top:151px;height:89px}
  .card-fatigue{top:252px;height:106px;padding-top:8px}
  .card-fatigue li.wrap{line-height:9.5px;padding-top:3px}
  .card-cough{top:366px;height:91px;padding-top:16px}
  .card-definition{top:469px;height:112px;padding-top:13px}
</style>
</head>
<body>
  <section class="spread">
    <svg class="spread-bands" width="798" height="616" viewBox="0 0 798 616" aria-hidden="true">
      <polygon points="35,0 370,0 700,616 330,616" fill="#ffffff" opacity=".22"/>
      <polygon points="370,0 420,0 798,420 798,520" fill="#ffffff" opacity=".18"/>
    </svg>

    <div class="brand brand-program">Breathe Forward<br>Rehab</div>

    <h2 class="intro-title">A path to Breathing Better</h2>
    <p class="intro-body">People diognosed with a chronic lung disease know that it is a serious<br>and debilitating condition requiring ongoing medical attention. But<br>many do not realize that pulmunory rehabilitattion may help them live<br>and breath better.</p>

    <h2 class="steps-title">The First Steps</h2>
    <p class="steps-body">Before you can start pulmonary<br>rehabilitation, a healthcare<br>provider will assess your health<br>status and develop a customized<br>plan based on your:</p>
    <ul class="bullets steps-list">
      <li>Physical well-being</li>
      <li>Emotional well-being</li>
      <li>Food Intake &amp; Nutrition</li>
    </ul>

    <h2 class="way-title">Along the way</h2>
    <ul class="bullets way-list">
      <li>Excercise specialist help improve endurance and muscle strength, to enhance your quality of life.</li>
      <li>Our healthcare team will help you better manage your lung Disease and avoid things that make it worse.</li>
      <li>Physical Therapists teach you energy conserving techniques and ways to breathe easier.</li>
    </ul>

    <div class="photo" role="img" aria-label="Photo of a cheerful group of adults raising their arms, holding a program sign"></div>

    <div class="brand brand-clinic"><span class="dot"></span><span>Clearway Lung Institute<br>of Houston</span></div>

    <h2 class="why-title">Why Pulmonary Theraphy?</h2>

    <div class="card card-breath">
      <h3>Shortness of Breath/Trouble Breathing</h3>
      <ul>
        <li>Strengthen lungs and sorrounding muscles</li>
        <li>Education on oxygen use</li>
        <li>Learn new breathing and oxygen conservation techniques</li>
      </ul>
    </div>

    <div class="card card-fatigue">
      <h3>Fatigue/Weakness</h3>
      <ul>
        <li>Increase stamina</li>
        <li>Strengthen key muscles</li>
        <li>Increase confidence</li>
        <li class="wrap">Get back in shape in a controlled, safe and supportive<br>&nbsp;environment</li>
      </ul>
    </div>

    <div class="card card-cough">
      <h3>Chronic Cough/Illness</h3>
      <ul>
        <li>Strengthen lungs</li>
        <li>Clear lungs using breathing tools and breathing techniques</li>
        <li>Build strength to fight future infection</li>
      </ul>
    </div>

    <div class="card card-definition">
      <h3>Definition of Pulmonary Theraphy</h3>
      <p>A program of education, excercise and training for those with<br>chronic and severe lung disease. Consist of both 1 on 1<br>theraphy and group theraphy sessions, 2-3 times per week<br>for 1 hour. Program ranges from 8-12 weeks depending on<br>doctor recommendation.</p>
    </div>
  </section>

  <div class="label">Inside Page</div>
</body>
</html>
```